URGENT Conference Banner ad to attract a crowd!

I need please in my brand colours 2 x static ads with this copy please:
Have an online business?
Make your customers stick!
It really needs to stand out but not be offensive.
I would like to see blue background on white font and then the reverse. on the white one, it needs a thin blue border around it.
I need it in static: 300x250 and 300x600.
on this one - 300x600. please add a circle saying register now!
Please see examples of other messages I have done. I need this URGENTLY pelase :)
Target Market(s)
http://www.tradefairvantora.com.au/en/home/
Industry/Entity Type
Business
Font styles to use
Other font styles liked:
- roboto font
Requirements
Must have
- Use this blue:
- 00b6ce
- roboto font
Nice to have
- look and feel like my banners supplied

```html
<!DOCTYPE html>
<html lang="en">
<head>
<meta charset="utf-8">
<title>Make Your Customers Stick – 300x600 Banner</title>
<link href="https://fonts.googleapis.com/css2?family=Roboto:wght@300;700&display=swap" rel="stylesheet">
<style>
  :root {
    --brand-blue: #00c2d6;
    --white: #ffffff;
    --page: #ffffff;
    --device-tint: rgba(255, 255, 255, 0.22);
    --button-shadow: rgba(0, 60, 70, 0.45);
  }
  html, body {
    margin: 0;
    padding: 0;
    width: 1200px;
    height: 1000px;
    overflow: hidden;
    background: var(--page);
  }
  .canvas {
    position: relative;
    width: 1200px;
    height: 1000px;
  }
  .banner {
    position: absolute;
    left: 445px;
    top: 234px;
    width: 302px;
    height: 600px;
    background: var(--brand-blue);
    overflow: hidden;
    color: var(--white);
    font-family: "Roboto", Arial, sans-serif;
  }
  .device-art {
    position: absolute;
    left: 0;
    top: 0;
    width: 302px;
    height: 600px;
  }
  .copy {
    position: absolute;
    left: 16px;
    top: 21px;
    right: 0;
  }
  .headline {
    margin: 0;
    font-weight: 700;
    font-size: 45.5px;
    line-height: 54px;
    letter-spacing: 0.2px;
    white-space: nowrap;
  }
  .subline {
    margin: 14px 0 0;
    font-weight: 300;
    font-size: 46px;
    line-height: 54px;
    letter-spacing: -0.3px;
    white-space: nowrap;
  }
  .register-button {
    position: absolute;
    left: 114px;
    top: 425px;
    width: 156px;
    height: 156px;
    border-radius: 50%;
    border: 1.5px solid var(--white);
    background: var(--brand-blue);
    box-shadow: 0 4px 16px var(--button-shadow);
    display: flex;
    align-items: center;
    justify-content: center;
    color: var(--white);
  }
  .register-label {
    font-family: "Roboto", Arial, sans-serif;
    font-weight: 700;
    font-size: 26px;
    line-height: 31px;
    letter-spacing: -0.5px;
    text-align: center;
    transform: rotate(5deg) scaleY(1.08);
    margin-top: -6px;
  }
</style>
</head>
<body>
<div class="canvas">
  <section class="banner">
    <svg class="device-art" viewBox="0 0 302 600" role="img" aria-label="Faint illustration of a tablet showing shop product tiles and a buy button">
      <rect x="80" y="118" width="240" height="320" rx="10" transform="rotate(7 200 278)" fill="var(--device-tint)"/>
    </svg>
    <div class="copy">
      <h1 class="headline">HAVE AN<br>ONLINE<br>BUSINESS?</h1>
      <p class="subline">Make your<br>customers<br>stick!</p>
    </div>
    <div class="register-button">
      <span class="register-label">REGISTER<br>NOW!</span>
    </div>
  </section>
</div>
</body>
</html>
```